Letterhead design for business

Looking for an attractive and professional letterhead that uses the logo that is attached below.

Target Market(s)

Potential bankruptcy clients.

Industry/Entity Type

Legal

Colors

Designer to choose colors to be used in the design.

Requirements
Must have
• Address for locations, phone number, and website address.
• Addresses are on website ferncoveadvice.example. Use following phone number (for tracking purposes): 555-013-8274

```html
<!DOCTYPE html>
<html lang="en">
<head>
<meta charset="utf-8">
<title>Ferncove Advice Law Group — Letterhead</title>
<link rel="stylesheet" href="https://fonts.googleapis.com/css2?family=Source+Sans+3:wght@400;600&family=Open+Sans:wght@600&display=swap">
<style>
  :root {
    --paper: #ffffff;
    --ink: #5a5a5c;
    --ink-dark: #3e3e40;
    --brand-green: #82bf88;
    --footer-text: #ffffff;
    --divider: rgba(255,255,255,0.9);
  }
  * { box-sizing: border-box; margin: 0; padding: 0; }
  html, body { width: 986px; height: 1200px; overflow: hidden; background: var(--paper); }
  .letterhead { position: relative; width: 986px; height: 1200px; overflow: hidden; background: var(--paper); font-family: "Source Sans 3", sans-serif; color: var(--ink); }

  .brand { position: absolute; left: 78px; top: 86px; display: flex; align-items: center; gap: 12px; }
  .brand-mark { width: 30px; height: 30px; border-radius: 50%; background: var(--brand-green); flex: none; }
  .brand-name { font-family: "Source Sans 3", sans-serif; font-weight: 600; font-size: 26px; color: var(--ink-dark); line-height: 1; }

  .letter-body { position: absolute; left: 71px; top: 226px; width: 841px; }
  .letter-body p { font-size: 18.6px; line-height: 24px; text-align: justify; margin-bottom: 24px; }

  .signature-block { position: absolute; left: 82px; top: 930px; }
  .signature-mark { width: 180px; height: 40px; background: linear-gradient(90deg, rgba(90,90,92,0.12), rgba(90,90,92,0.04)); }
  .signer-name { margin: 4px 0 0 46px; font-size: 18px; color: var(--ink); }

  .contact-band { position: absolute; left: 0; top: 1087px; width: 986px; height: 71px; background: var(--brand-green); display: flex; align-items: center; font-family: "Open Sans", sans-serif; font-weight: 600; font-size: 11.5px; color: var(--footer-text); }
  .contact-item { display: flex; align-items: center; gap: 6px; padding: 0 16px; height: 38px; white-space: nowrap; }
  .contact-item + .contact-item { border-left: 2px solid var(--divider); }
  .contact-item:first-child { padding-left: 28px; padding-right: 24px; }
  .contact-item svg { width: 11px; height: 11px; fill: var(--footer-text); flex: none; }
</style>
</head>
<body>
<main class="letterhead">
  <header class="brand">
    <span class="brand-mark"></span>
    <span class="brand-name">Ferncove Advice Law Group</span>
  </header>

  <section class="letter-body">
    <p>Lorem ipsum dolor sit amet, consectetur adipiscing elit, sed do eiusmod tempor incididunt ut labore et dolore magna aliqua. Ut enim ad minim veniam, quis nostrud exercitation ullamco laboris nisi ut aliquip ex ea commodo consequat. Duis aute irure dolor in reprehenderit in voluptate velit esse cillum dolore eu fugiat nulla pariatur. Excepteur sint occaecat cupidatat non proident, sunt in culpa qui officia deserunt mollit anim id est laborum</p>
    <p>Sed ut perspiciatis unde omnis iste natus error sit voluptatem accusantium doloremque laudantium, totam rem aperiam, eaque ipsa quae ab illo inventore veritatis et quasi architecto beatae vitae dicta sunt explicabo. Nemo enim ipsam voluptatem quia voluptas sit aspernatur aut odit aut fugit, sed quia consequuntur magni dolores eos qui ratione voluptatem sequi nesciunt. Neque porro quisquam est, qui dolorem ipsum quia dolor sit amet, consectetur, adipisci velit, sed quia non numquam eius modi tempora incidunt ut labore et dolore magnam aliquam quaerat voluptatem. Ut enim ad minima veniam, quis nostrum exercitationem ullam corporis suscipit laboriosam, nisi ut aliquid ex ea commodi consequatur? Quis autem vel eum iure reprehenderit qui in ea voluptate velit esse quam nihil molestiae consequatur, vel illum qui dolorem eum fugiat quo voluptas nulla pariatur?</p>
    <p>Lorem ipsum dolor sit amet, consectetur adipiscing elit, sed do eiusmod tempor incididunt ut labore et dolore magna aliqua. Ut enim ad minim veniam, quis nostrud exercitation ullamco laboris nisi ut aliquip ex ea commodo consequat. Duis aute irure dolor in reprehenderit in voluptate velit esse cillum dolore eu fugiat nulla pariatur. Excepteur sint occaecat cupidatat non proident, sunt in culpa qui officia deserunt mollit anim id est laborum</p>
    <p>Sed ut perspiciatis unde omnis iste natus error sit voluptatem accusantium doloremque laudantium, totam rem aperiam, eaque ipsa quae ab illo inventore veritatis et quasi architecto beatae vitae dicta sunt explicabo. Nemo enim ipsam voluptatem quia voluptas sit aspernatur aut odit aut fugit, sed quia consequuntur magni dolores eos qui ratione voluptatem sequi nesciunt. Neque porro quisquam est, qui dolorem ipsum quia dolor sit amet, consectetur, adipisci velit, sed quia non numquam eius modi tempora incidunt ut labore et dolore magnam aliquam quaerat voluptatem. Ut enim ad minima</p>
  </section>

  <section class="signature-block">
    <div class="signature-mark" role="img" aria-label="Handwritten signature"></div>
    <p class="signer-name">Name Name</p>
  </section>

  <footer class="contact-band">
    <div class="contact-item">48 Linden Row, Suite #310 Brookfield, Georgia 30000</div>
    <div class="contact-item">
      <svg viewBox="0 0 24 24" aria-hidden="true"><path d="M6.6 10.8a15.1 15.1 0 0 0 6.6 6.6l2.2-2.2a1 1 0 0 1 1-.25 11.4 11.4 0 0 0 3.6.57 1 1 0 0 1 1 1V20a1 1 0 0 1-1 1A17 17 0 0 1 3 4a1 1 0 0 1 1-1h3.5a1 1 0 0 1 1 1c0 1.25.2 2.45.57 3.570a1 1 0 0 1-.25 1z"/></svg>
      555-013-8274
    </div>
    <div class="contact-item">
      <svg viewBox="0 0 24 24" aria-hidden="true"><path d="M2 5h20v2l-10 6L2 7z M2 9l10 6 10-6v10H2z"/></svg>
      info@ferncoveadvice.example
    </div>
    <div class="contact-item">
      <svg viewBox="0 0 24 24" aria-hidden="true"><path d="M12 2a10 10 0 1 0 0 20 10 10 0 0 0 0-20zm6.9 9h-3a15 15 0 0 0-1.3-5.6A8 8 0 0 1 18.9 11zM12 4.1c.9 1.2 1.8 3.5 2 6.9h-4c.2-3.4 1.1-5.7 2-6.9zM9.4 5.4A15 15 0 0 0 8.1 11h-3a8 8 0 0 1 4.3-5.6zM5.1 13h3a15 15 0 0 0 1.3 5.6A8 8 0 0 1 5.1 13zm6.9 6.9c-.9-1.2-1.8-3.5-2-6.9h4c-.2 3.4-1.1 5.7-2 6.9zm2.6-1.3a15 15 0 0 0 1.3-5.6h3a8 8 0 0 1-4.3 5.6z"/></svg>
      www.ferncoveadvice.example
    </div>
  </footer>
</main>
</body>
</html>
```